Banner Ad and Digital Ad design for tradeshow

I need two graphics designed (can be same/similar design just different dimensions. We are an engineering firm practicing in the solid waste industry. We are a conference sponsor and need two graphics.
(1) Banner Ad - 300x250 - gif, png, jped, html, or other. Imagery with our mantra - Driven by purpose. Guided by stewardship. Striving for excellence.
(2) Digital Ad (static) - 1920x1080 hi-res jpg or png.

Target Market(s)

Solid Waste Management Industry (Environmental)

Industry/Entity Type

Environmental

Requirements
Must have
• Quality Aesthetic
Nice to have
• Great Imagery + our mantra

```html
<!DOCTYPE html>
<html lang="en">
<head>
<meta charset="utf-8">
<title>Kestrel Engineering – Sponsor Ad</title>
<link rel="stylesheet" href="https://fonts.googleapis.com/css2?family=Outfit:wght@500&display=swap">
<style>
  :root {
    --canvas-bg: #dde2de;
    --sage: #6f8169;
    --earth: #6e5f3d;
    --headline: #6c5d3c;
    --frame: #ffffff;
    --photo-sky: #c9c6bd;
    --photo-soil: #7a5f44;
    --ghost-mark: #c9cfcb;
  }
  html, body {
    margin: 0;
    padding: 0;
    width: 1200px;
    height: 675px;
    overflow: hidden;
    background: var(--canvas-bg);
  }
  .ad {
    position: relative;
    width: 1200px;
    height: 675px;
    overflow: hidden;
    background: linear-gradient(160deg, #e3e7e3 0%, var(--canvas-bg) 60%, #d7ddd9 100%);
    font-family: "Outfit", sans-serif;
  }
  .ad__shapes {
    position: absolute;
    inset: 0;
  }
  .brand {
    position: absolute;
    left: 759px;
    top: 125px;
    display: flex;
    align-items: center;
    gap: 22px;
    color: var(--sage);
    font-weight: 500;
  }
  .brand__square {
    width: 82px;
    height: 82px;
    background: var(--sage);
    border-radius: 6px;
  }
  .brand__name {
    display: flex;
    flex-direction: column;
    line-height: 1;
  }
  .brand__primary {
    font-size: 52px;
    letter-spacing: 2px;
  }
  .brand__secondary {
    font-size: 24px;
    letter-spacing: 9.5px;
    margin-top: 8px;
  }
  .mantra {
    position: absolute;
    right: 41px;
    top: 250px;
    margin: 0;
    text-align: right;
    color: var(--headline);
    font-weight: 500;
    font-size: 61px;
    line-height: 67px;
    white-space: nowrap;
    letter-spacing: 0.2px;
  }
  .mantra span { display: block; }
</style>
</head>
<body>
<div class="ad">
  <svg class="ad__shapes" width="1200" height="675" viewBox="0 0 1200 675">
    <defs>
      <linearGradient id="fieldPhoto" x1="0" y1="0" x2="0" y2="1">
        <stop offset="0" stop-color="var(--photo-sky)"/>
        <stop offset="0.12" stop-color="#8f8a74"/>
        <stop offset="0.3" stop-color="#8a6d50"/>
        <stop offset="1" stop-color="var(--photo-soil)"/>
      </linearGradient>
    </defs>

    <!-- top-right sage corner -->
    <path d="M884 0 C 930 40, 950 78, 1010 78 L 1200 78 L 1200 0 Z"
          fill="var(--frame)"/>
    <path d="M896 0 C 940 36, 960 70, 1014 70 L 1200 70 L 1200 0 Z"
          fill="var(--sage)"/>

    <!-- ghost square decoration -->
    <rect class="ghost-mark" x="38" y="472" width="169" height="169" rx="8"
          fill="var(--ghost-mark)" opacity="0.7"/>

    <!-- bottom earth band -->
    <path d="M274 675 L 370 592 C 384 581, 392 577, 410 577 L 1010 577 C 1090 577, 1150 520, 1200 460 L 1200 675 Z"
          fill="var(--frame)"/>
    <path d="M289 675 L 382 596 C 394 589, 400 588, 414 588 L 1012 588 C 1095 588, 1155 535, 1200 486 L 1200 675 Z"
          fill="var(--earth)"/>

    <!-- site photo frame -->
    <path d="M0 0 L 624 0 L 300 310 C 270 340, 240 362, 190 362 L 0 362 Z"
          fill="var(--frame)"/>
    <path d="M0 0 L 606 0 L 288 300 C 260 328, 232 348, 186 348 L 0 348 Z"
          fill="url(#fieldPhoto)" role="img"
          aria-label="Photo: two engineers in hi-vis clothing surveying a graded landfill site with facility buildings in the distance"/>
  </svg>

  <div class="brand" aria-label="Kestrel Engineering">
    <div class="brand__square"></div>
    <div class="brand__name">
      <span class="brand__primary">KESTREL</span>
      <span class="brand__secondary">ENGINEERING</span>
    </div>
  </div>

  <h1 class="mantra">
    <span>DRIVEN BY PURPOSE.</span>
    <span>GUIDED BY STEWARDSHIP.</span>
    <span>STRIVING FOR EXCELLENCE.</span>
  </h1>
</div>
</body>
</html>
```